New Business Card Design for Engineering and Surveying Company

We need a new design template for our business cards. We are a civil engineering, land surveying and pipeline integrity business. Please see dkhpartners.com for details. We need a bold, new business card design to complement our rebranding and marketing program. We have anew logo and attached vectro file. Please find additional details below. I am available to answer any questions.

Target Market(s)

Contractors, business owners, oil companies

Contact Information for Business Card

Needs to be customizable for different people (name, title, cell)

Font styles to use
Sans Serif
Other font styles liked:
• See eps file

Requirements
Must have
• Example Information:
Trevor Ashcombe

T:936-555-0173
M: 346-555-0148
tashcombe@dkhprtnrs.com

Address: 1875 Pinecrest Parkway, Harlow Springs, Texas 75921
Email: tolvanrey@dkhpartners.com
Website: www.dkhpartners.com
Nice to have
• I would like the back of the card to have the logo on a bold background with the text below:

[logo]
DORAN KESSLING & PARTNERS
CIVIL ENGINEERING | LAND SURVEYING | PIPELINE INTEGRITY

The reverse side should have the contact information for the person (example above), a smaller version of the logo and a graphic

```html
<!DOCTYPE html>
<html lang="en">
<head>
<meta charset="utf-8">
<title>DKP Business Card</title>
<link href="https://fonts.googleapis.com/css2?family=Roboto:wght@300;400;500;700;900&display=swap" rel="stylesheet">
<style>
  :root {
    --stage: #2a2a2c;
    --card: #1c1c1e;
    --white: #f4f4f4;
    --grey: #d9d9d9;
    --rule: #8a8a8a;
    --red: #e0202e;
  }
  * { margin: 0; padding: 0; box-sizing: border-box; }
  html, body { width: 1200px; height: 1108px; overflow: hidden; }
  body {
    background: var(--stage);
    font-family: "Roboto", Arial, sans-serif;
    position: relative;
  }
  .card {
    position: absolute;
    top: 214px;
    width: 410px;
    height: 680px;
    background: var(--card);
    border-radius: 26px;
    box-shadow: 0 18px 40px rgba(0,0,0,0.45);
    text-align: center;
    overflow: hidden;
  }
  .card--front { left: 150px; }
  .card--back { left: 640px; }

  .wordmark {
    font-weight: 900;
    color: var(--white);
    letter-spacing: 2px;
    line-height: 1;
  }
  .card--front .wordmark { font-size: 92px; margin-top: 110px; }
  .card--back .wordmark { font-size: 104px; margin-top: 80px; }

  .person-name {
    margin-top: 62px;
    color: var(--red);
    font-weight: 700;
    font-size: 27px;
    letter-spacing: 0.5px;
    text-transform: uppercase;
  }
  .icon-rule {
    display: flex;
    align-items: center;
    justify-content: center;
    gap: 10px;
    margin: 14px 60px 0;
  }
  .icon-rule .line { flex: 1; height: 1px; background: var(--rule); }
  .icon-rule .icons { display: flex; gap: 5px; }
  .icon-rule svg { width: 26px; height: 26px; display: block; }

  .contact-list {
    list-style: none;
    margin-top: 26px;
    color: var(--grey);
    font-weight: 300;
    font-size: 21px;
    line-height: 31px;
  }
  .contact-list .domain { color: var(--red); }
  .divider { height: 1px; background: var(--rule); margin: 26px 90px 0; }
  .address {
    margin-top: 28px;
    color: var(--grey);
    font-weight: 300;
    font-size: 21px;
    line-height: 30px;
    font-style: normal;
  }

  .company-name {
    margin-top: 44px;
    color: var(--red);
    font-weight: 500;
    font-size: 27px;
  }
  .services {
    margin-top: 10px;
    color: var(--grey);
    font-weight: 300;
    font-size: 22px;
    line-height: 32px;
  }
  .services .sep { margin: 0 10px; }
  .decor-field {
    position: absolute;
    left: 0; right: 0; bottom: 0;
    height: 330px;
    background: radial-gradient(ellipse at 40% 70%, #4a4a4d 0%, #2c2c2f 40%, var(--card) 75%);
  }
</style>
</head>
<body>
  <section class="card card--front">
    <div class="wordmark">DKP</div>
    <h1 class="person-name">Trevor Ashcombe</h1>
    <div class="icon-rule">
      <span class="line"></span>
      <span class="icons">
        <svg viewBox="0 0 26 26" aria-label="Phone"><circle cx="13" cy="13" r="13" fill="#e0202e"/><path d="M8 8c1-1 2-1 2.5 0l1 2c.3.6 0 1-.5 1.4l-.6.5c.6 1.5 1.7 2.6 3.2 3.2l.5-.6c.4-.5.8-.8 1.4-.5l2 1c1 .5 1 1.5 0 2.5-1.5 1.5-4 .6-6.3-1.7S6.5 9.5 8 8z" fill="#1c1c1e"/></svg>
        <svg viewBox="0 0 26 26" aria-label="Mobile"><circle cx="13" cy="13" r="13" fill="#e0202e"/><rect x="9.5" y="6.5" width="7" height="13" rx="1.2" fill="#1c1c1e"/><rect x="10.7" y="8" width="4.6" height="8.5" fill="#e0202e"/></svg>
        <svg viewBox="0 0 26 26" aria-label="Email"><circle cx="13" cy="13" r="13" fill="#e0202e"/><rect x="7" y="9" width="12" height="8.5" rx="1" fill="#1c1c1e"/><path d="M7.5 9.5 13 14l5.5-4.5" stroke="#e0202e" stroke-width="1.2" fill="none"/></svg>
        <svg viewBox="0 0 26 26" aria-label="Website"><circle cx="13" cy="13" r="13" fill="#e0202e"/><circle cx="13" cy="13" r="6" fill="none" stroke="#1c1c1e" stroke-width="1.6"/><ellipse cx="13" cy="13" rx="2.6" ry="6" fill="none" stroke="#1c1c1e" stroke-width="1.3"/><path d="M7 13h12" stroke="#1c1c1e" stroke-width="1.3"/></svg>
      </span>
      <span class="line"></span>
    </div>
    <ul class="contact-list">
      <li>936-555-0173</li>
      <li>346-555-0148</li>
      <li>tashcombe@dkhprtnrs.com</li>
      <li>www.<span class="domain">dkhpartners</span>.com</li>
    </ul>
    <div class="divider"></div>
    <address class="address">1875 Pinecrest Parkway<br>Harlow Springs, Texas 75921</address>
  </section>

  <section class="card card--back">
    <div class="wordmark">DKP</div>
    <h2 class="company-name">Doran Kessling &amp; Partners</h2>
    <p class="services">Civil Engineering<br>Land Surveying<span class="sep">|</span>Pipeline Integrity</p>
    <div class="decor-field" role="img" aria-label="Large faint brand emblem decoration in dark grey tones"></div>
  </section>
</body>
</html>
```